Trifold brochure for Thai yoga massage practice (In a Combat gym and a Spa)

I am a Practitioner of Thai massage in Toronto, and will in the near future be offering personal training with transitional fitness from couch potato to weekend warriors.

I train in Muay-thai and my current stream of clients are "thai tigers" in need of restorative therapy to get them back on their feet - hence the website name Fernquiet.com.
My other stream of clients are in a Lovely Spa on a rooftop patio (if you're ever in Toronto come on by).

So I have the best of two worlds (injuries vs. pure bliss) Dark vs. Light

I want to introduce Thai yoga massage to a new modern audience. Thai massage is an ancient, effective hybrid therapy incorporating traditional acupressure/ body meridian therapy and human kinetics simultaneously.

Brochures are meant for distribution to martial arts studios, fitness gyms and other spas.

I am open to eye-catching, out of the box ideas.

My website: www.fernquiet.com (I am in the process of editing this new web space - apologies for the very basic nature of it)

Pictures are attached for review or view my link:
https://files.plumdock.net/share?id=7QX41mKpLw93_rTbNvEhYcUaZdJ2&view=open

Thank you!

Target Market(s)

20-45 year old fitness enthusiast for a gym audience
or 20-55 year old looking for general wellness/ relaxation
or combination of both (yin/yang type design)

Industry/Entity Type

Training

Font styles to use
Decorative

Requirements
Must have
• Will be looking for innovation, clever, witty design, please be creative. Toronto is a quirky city, I welcome quirky, yet tasteful designs.

Please use a good amount of flow, and streaming lines.
Nice to have
• If we could have a yin / yang effect that would be nice (Combat restoration vs. Relaxation)
Should not have
• Please do not have text / designs that convey the stereotypical nonsense that surround Asian based massage (my cup is full already).

```html
<!DOCTYPE html>
<html lang="en">
<head>
<meta charset="utf-8">
<title>Fern Quiet – Trifold Brochure</title>
<link href="https://fonts.googleapis.com/css2?family=Josefin+Sans:wght@300;400&family=Montserrat:wght@500;700&family=Open+Sans:wght@400;600&display=swap" rel="stylesheet">
<style>
  :root {
    --bg: #c9cdd1;
    --paper: #ffffff;
    --coral: #f08a70;
    --teal: #1f7d8c;
    --teal-deep: #14606c;
    --sand: #d8cec4;
    --ink: #2b2b2b;
    --night: #1b1e21;
    --light: #f4f1ee;
  }
  * { box-sizing: border-box; margin: 0; padding: 0; }
  html, body { width: 1200px; height: 800px; overflow: hidden; }
  body { background: var(--bg); font-family: "Open Sans", sans-serif; color: var(--ink); }

  .brochure {
    position: absolute; left: 120px; top: 30px;
    width: 960px; height: 740px;
    display: flex;
    box-shadow: 0 14px 30px rgba(0,0,0,.18);
  }
  .panel {
    position: relative; width: 320px; height: 740px;
    background: var(--paper); overflow: hidden;
  }
  .panel + .panel { box-shadow: inset 6px 0 8px -6px rgba(0,0,0,.18); }
  .panel-art, .photo { position: absolute; left: 0; top: 0; width: 320px; height: 740px; }

  /* Left panel */
  .heat-title {
    position: absolute; left: 30px; top: 210px; width: 260px;
    font-family: "Montserrat", sans-serif; font-weight: 500;
    font-size: 21px; letter-spacing: .5px; color: var(--teal);
  }
  .heat-copy {
    position: absolute; left: 30px; top: 250px; width: 260px;
    font-size: 11.5px; line-height: 17px; text-align: justify; color: var(--ink);
  }

  /* Middle panel */
  .venues {
    position: absolute; left: 20px; top: 40px; width: 280px;
    text-align: center; font-size: 11px; line-height: 16px;
  }
  .venue + .venue { margin-top: 26px; }
  .venue-name {
    font-family: "Montserrat", sans-serif; font-weight: 700;
    font-size: 11px; color: var(--teal); letter-spacing: .3px; margin-bottom: 2px;
  }
  .venue-hours { margin-top: 14px; }

  /* Brand lockup */
  .brand { position: absolute; left: 0; width: 320px; text-align: center; }
  .brand-mark {
    width: 46px; height: 46px; border-radius: 50%;
    background: var(--coral); margin: 0 auto 10px;
  }
  .brand-name {
    font-family: "Josefin Sans", sans-serif; font-weight: 300;
    font-size: 30px; letter-spacing: 2px; color: var(--light);
  }
  .brand-tagline {
    font-family: "Josefin Sans", sans-serif; font-weight: 400;
    font-size: 10px; letter-spacing: 1px; line-height: 14px;
    color: var(--light); margin-top: 6px;
  }
  .brand--inside { top: 588px; }
  .brand--inside .brand-name { font-size: 24px; }
  .brand--cover { top: 56px; }
</style>
</head>
<body>
<main class="brochure">

  <!-- Inside left: heat therapy -->
  <section class="panel panel--heat">
    <svg class="panel-art" viewBox="0 0 320 740" aria-hidden="true">
      <polygon points="0,0 320,0 320,100 160,168 0,100" fill="var(--coral)"/>
      <polygon points="0,100 160,168 320,100 320,118 160,186 0,118" fill="var(--teal)"/>
      <polygon points="0,118 160,186 320,118 320,124 160,192 0,124" fill="var(--sand)"/>
    </svg>
    <h2 class="heat-title">THAI HEAT THERAPY</h2>
    <p class="heat-copy">Lorem ipsum dolor sit amet, consectetuer adipiscing elit, sed diam nonummy nibh euismod tincidunt ut laoreet dolore magna aliquam erat volutpat. Ut wisi enim ad minim veniam, quis nostrud exerci tation ullamcorper suscipit lobortis nisl ut aliquip ex ea commodo consequat. Duis autem vel eum iriure dolor in hendrerit in vulputate velit esse molestie consequat, vel illum dolore eu feugiat nulla facilisis at vero eros et accumsan et iusto odio dignissim qui blandit praesent luptatum zzril delenit augue duis dolore te feugait nulla facilisi. Nam liber tempor cum soluta nobis eleifend option congue nihil imperdiet doming id quod mazim placerat facer possim assum. Typi non habent claritatem insitam; est usus legentis in iis qui facit eorum claritatem. Investigationes demonstraverunt lectores legere me lius quod ii legunt saepius. Claritas est etiam processus dynamicus, qui sequitur.</p>
  </section>

  <!-- Back: venues -->
  <section class="panel panel--venues">
    <svg class="panel-art" viewBox="0 0 320 740" aria-hidden="true">
      <path d="M0,405 Q160,470 320,395 L320,740 L0,740 Z" fill="var(--sand)"/>
      <path d="M0,438 Q160,500 320,428 L320,740 L0,740 Z" fill="var(--coral)"/>
    </svg>
    <svg class="photo" viewBox="0 0 320 740" role="img" aria-label="Black and white photo of a gym training session">
      <defs>
        <linearGradient id="gymPhoto" x1="0" y1="0" x2="1" y2="1">
          <stop offset="0" stop-color="#4a4d50"/>
          <stop offset="1" stop-color="var(--night)"/>
        </linearGradient>
      </defs>
      <path d="M0,468 Q160,528 320,458 L320,740 L0,740 Z" fill="url(#gymPhoto)"/>
    </svg>
    <div class="venues">
      <div class="venue">
        <h3 class="venue-name">KOVAN RIDGE GYM: COMBAT / SELF DEFENSE</h3>
        <p>1840 Larchmont Avenue, Toronto, ON M2B 4K7</p>
        <p>www.kovanridge.com</p>
        <p class="venue-hours">Monday, Wednesday 5:30 - 8:30 pm<br>Thursday 6:00 - 8:30 pm<br>Friday 6:00 - 8:30 pm</p>
      </div>
      <div class="venue">
        <h3 class="venue-name">WILLOW SALON | SPA</h3>
        <p>318 Birchwell Avenue, Toronto, ON M3R 2P5</p>
        <p>www.willowspa.com</p>
        <p class="venue-hours">Sunday 12:00-4:00 pm</p>
      </div>
    </div>
    <div class="brand brand--inside">
      <div class="brand-mark"></div>
      <p class="brand-name">FERN QUIET</p>
      <p class="brand-tagline">SPECIALIZED IN THAI YOGA MASSAGE,<br>THAI HEAT THERAPY</p>
    </div>
  </section>

  <!-- Front cover -->
  <section class="panel panel--cover">
    <svg class="photo" viewBox="0 0 320 740" role="img" aria-label="Teal and black tiger stripe pattern">
      <defs>
        <linearGradient id="stripeField" x1="0" y1="0" x2="1" y2="1">
          <stop offset="0" stop-color="var(--teal-deep)"/>
          <stop offset=".5" stop-color="#10363c"/>
          <stop offset="1" stop-color="var(--teal)"/>
        </linearGradient>
      </defs>
      <rect width="320" height="380" fill="url(#stripeField)"/>
    </svg>
    <svg class="panel-art" viewBox="0 0 320 740" aria-hidden="true">
      <path d="M0,330 Q170,380 320,315 L320,740 L0,740 Z" fill="var(--sand)"/>
      <path d="M0,365 Q170,415 320,350 L320,740 L0,740 Z" fill="var(--coral)"/>
    </svg>
    <svg class="photo" viewBox="0 0 320 740" role="img" aria-label="Photo of a practitioner giving a Thai yoga massage on a mat">
      <defs>
        <linearGradient id="massagePhoto" x1="0" y1="0" x2="1" y2="1">
          <stop offset="0" stop-color="#2a2527"/>
          <stop offset=".6" stop-color="#5a2a2c"/>
          <stop offset="1" stop-color="#b8363a"/>
        </linearGradient>
      </defs>
      <path d="M0,392 Q170,440 320,378 L320,740 L0,740 Z" fill="url(#massagePhoto)"/>
    </svg>
    <div class="brand brand--cover">
      <div class="brand-mark"></div>
      <p class="brand-name">FERN QUIET</p>
      <p class="brand-tagline">SPECIALIZED IN THAI YOGA MASSAGE,<br>THAI HEAT THERAPY</p>
    </div>
  </section>

</main>
</body>
</html>
```